Elegant and modern body scrub for organic junkies

I need a package design for my new company based out of Austin, Texas. We are focused on cruelty free and all natural and organic products. Our deign needs to be able to have the information we require on it, while still appearing very clean and captivating. Our initial product is a clear skin body scrub, intended for people with problematic skin. Our target market is women and we want to show elegance, without appearing "high end."
Updates

Reason: I want to allot more time for certain designers to submit edits. Last minute proposals have been appealing

Target Market(s)

Women. Organic and holistic minded. Natural beauty lovers.

Industry/Entity Type

Skin Care Product

Font styles to use
Script
Other font styles liked:
• AmericanTypewriter, Beautifulflaws, courier, caviarDreams-bold

Colors
000000
ffc214
ffffff
fece3e
fbee3e

Requirements
Must have
• Must be designed in Adobe Illustrator.
• The photo titled “structure for oz and grams” -That needs to be included at the bottom of 1B. I like the horizontal and vertical bar that separate the two. I want that.
• Color Inspiration - The photo titled “venra color inspiration” and “color combo inspiration” are the colors I want. BLACK, GOLD, WHITE. I want the label background black and the writing in white with some gold somewhere on it. My logo is going to be a golden elephant.
• The photos titled “I like how clean this looks” and “I also like how clean this looks” - I want 1B to look super clean. I don’t want a lot of information in this box. I want simple and clean. This is where the logo and brand name will go.
• Logo - A golden elephant. I want it to be gold and geometric. There can be dimension like this elephant example on the left of the 1B description. I want the trunk to be facing to the left and the trunk needs to be raised overhead and touching the animal's forehead.
• The photo titled “sideways writing and silver rim” - I want 1C to be written sideways like this. My text will be much more extensive so the font won’t be able to be so big.
Nice to have
• The photo titled “sideways writing and silver rim” - I want 1C to be written sideways like this. My text will be much more extensive so the font won’t be able to be so big. I also REALLY like how this label is rimmed in silver, but I would want gold. This is not mandatory, but I really like this.
• The photo titled “melted honey” - This is another option I really like. The gold that looks like honey dripping on the label is really cool. Not mandatory, but I really liked that. I also like the craft background on this.
• Color Inspiration - The photo titled “color inspiration” and “another color inspiration” is an option I would also like to see. Rather than black, I’d like to see what it would ALSO look like with a navy background. NAVY, GOLD, WHITE, maybe black somewhere.
Should not have
• Colorful patterns or excessive info in section 1B.

```html
<!DOCTYPE html>
<html lang="en">
<head>
<meta charset="utf-8">
<title>Clear Skin Body Polish – Label</title>
<link href="https://fonts.googleapis.com/css2?family=Kaushan+Script&family=Courier+Prime&display=swap" rel="stylesheet">
<style>
  :root {
    --page: #f2f2f2;
    --label-black: #000000;
    --panel-black: #1b1b1b;
    --panel-glow: #262626;
    --gold: #f2a81d;
    --gold-light: #fece3e;
    --gold-deep: #c98a12;
    --gold-haze: rgba(242, 168, 29, 0.28);
    --gold-haze-soft: rgba(242, 168, 29, 0.10);
    --white: #f4f4f4;
    --muted: #9a9a9a;
  }
  * { margin: 0; padding: 0; box-sizing: border-box; }
  html, body {
    width: 1200px; height: 1200px; overflow: hidden;
    background: var(--page);
  }
  .label {
    position: absolute; left: 100px; top: 195px;
    width: 1000px; height: 810px;
    background: var(--label-black);
    overflow: hidden;
  }
  .ornament {
    position: absolute; top: 36px; height: 732px; width: 140px;
  }
  .ornament--left {
    left: 36px;
    background: radial-gradient(ellipse 100% 50% at 100% 50%,
      var(--gold-haze) 0%, var(--gold-haze-soft) 60%, transparent 100%);
  }
  .ornament--right {
    left: 812px;
    background: radial-gradient(ellipse 100% 50% at 0% 50%,
      var(--gold-haze) 0%, var(--gold-haze-soft) 60%, transparent 100%);
  }
  .gold-rule {
    position: absolute; top: 0; width: 6px; height: 810px;
    background: var(--gold);
  }
  .gold-rule--left { left: 176px; }
  .gold-rule--right { left: 791px; }
  .front-panel {
    position: absolute; left: 182px; top: 0; width: 609px; height: 810px;
    background:
      radial-gradient(circle at 50% 22%, var(--panel-glow) 0 300px, transparent 302px),
      var(--panel-black);
  }
  .brand-name {
    position: absolute; left: 0; right: 0; top: 92px;
    text-align: center;
    font-family: "Kaushan Script", cursive;
    font-size: 100px; line-height: 1;
    color: var(--gold);
  }
  .emblem {
    position: absolute; left: 184px; top: 250px;
    width: 250px; height: 255px;
    border-radius: 50%;
    background: radial-gradient(circle at 45% 45%, var(--gold-light) 0%, var(--gold) 40%, rgba(201,138,18,0.35) 68%, transparent 72%);
  }
  .product-band {
    position: absolute; left: -3px; top: 554px; width: 615px; height: 110px;
    border-top: 2px solid var(--gold);
    border-bottom: 2px solid var(--gold);
    background: #131313;
    text-align: center;
    font-family: "Courier Prime", "Courier New", monospace;
    color: var(--white);
  }
  .product-band__line1 {
    margin-top: 12px;
    font-size: 41px; letter-spacing: 3px; line-height: 1.1;
  }
  .product-band__line2 {
    font-size: 48px; letter-spacing: 3px; line-height: 1.1;
  }
  .net-weight {
    position: absolute; left: 0; right: 0; top: 744px;
    text-align: center;
    font-family: "Courier Prime", "Courier New", monospace;
    font-size: 25px; letter-spacing: 3px;
    color: var(--muted);
    word-spacing: 12px;
  }
</style>
</head>
<body>
  <div class="label">
    <div class="ornament ornament--left" role="img" aria-label="Delicate gold mandala-style ornament running down the left side"></div>
    <div class="gold-rule gold-rule--left"></div>
    <div class="front-panel">
      <div class="brand-name">Brand Name</div>
      <div class="emblem" role="img" aria-label="Golden elephant emblem with raised trunk"></div>
      <div class="product-band">
        <p class="product-band__line1">Clear Skin</p>
        <p class="product-band__line2">Body Polish</p>
      </div>
      <p class="net-weight">12 oz | 340g</p>
    </div>
    <div class="gold-rule gold-rule--right"></div>
    <div class="ornament ornament--right" role="img" aria-label="Delicate gold mandala-style ornament running down the right side"></div>
  </div>
</body>
</html>
```